Bright Harbor Real Estate Institute

This must be done in word press and I will need about 7 tabs The home page, Information page, Schedule and Cost page which will link to a Email me form, a online registration a about us and location/contact tab Each tab will then open several other pages. The home page will describe different courses that we offer since all the schools are about the same you can get a good ideal by going to qelvanto.org or pinnaclebayrealtyschool.com and looking at their site I would like mine to be similar as the courses are exactly the same but I would like the site to be more modern I also need it to be in word press so I can change it and update the dates as they change I have attached he logo below

Target Market(s)

people interested in getting into real estate and those who need continuing education

Coding

Coded - Design and coding required

Number of Pages Required

5+ page

Font styles to use
Sans Serif

Colors
3276b5

Requirements
Must have
• A page to schedule classes, a tab so the college I am partnering with can link the online courses to the back side, a page that describes the type of classes I offer

```html
<!DOCTYPE html>
<html lang="en">
<head>
<meta charset="utf-8">
<title>Bright Harbor Real Estate Institute</title>
<link href="https://fonts.googleapis.com/css2?family=Poppins:wght@300;400;500;600;700&display=swap" rel="stylesheet">
<style>
:root{
  --brand:#3276b5;
  --brand-dark:#2a68a3;
  --ink:#222;
  --text:#444;
  --muted:#666;
  --line:#d9d9d9;
  --white:#fff;
}
*{margin:0;padding:0;box-sizing:border-box}
html,body{width:1200px;height:2735px;overflow:hidden;background:var(--white)}
body{position:relative;font-family:'Poppins',sans-serif;color:var(--text)}
.abs{position:absolute}

.top-nav{left:0;top:0;width:1200px;height:42px;background:var(--brand);display:flex;justify-content:space-between;align-items:center;padding:0 141px 0 143px}
.top-nav a,.footer-nav a{color:var(--white);text-decoration:none;font-size:12.5px;font-weight:500;letter-spacing:.3px}

.site-header{left:0;top:42px;width:1200px;height:117px;background:#fcfcfc}
.brand-name{left:143px;top:70px;display:flex;align-items:center;gap:10px;color:var(--brand);font-weight:600}
.brand-dot{width:30px;height:30px;border-radius:50%;background:var(--brand);flex:none}
.brand-name span{font-size:22px;line-height:25px;display:block}
.contact-item{top:76px;display:flex;gap:10px;align-items:flex-start}
.contact-item .label{color:var(--brand);font-weight:600;font-size:15px;line-height:18px}
.contact-item .value{color:#444;font-size:17px;line-height:22px}
.contact-item svg{margin-top:4px}

.hero{left:0;top:159px;width:1200px;height:459px;background:linear-gradient(90deg,#6e6358 0%,#8c857d 30%,#b9b3aa 52%,#e6e3df 68%,#fff 80%)}
.hero-text{right:143px;top:318px;text-align:right;color:#111;font-size:24px;font-weight:500;line-height:34px}

.feature{top:685px;width:280px;text-align:center}
.feature h3{margin-top:12px;font-size:19px;font-weight:600;color:var(--ink)}
.feature p{margin-top:8px;font-size:12.5px;line-height:22px;color:var(--muted);font-weight:300}
.learn{display:inline-flex;align-items:center;gap:6px;margin-top:6px;color:var(--brand);font-size:12.5px;font-weight:500;text-decoration:none}

.about{left:143px;top:1090px;width:425px}
.about .eyebrow{font-size:14px;font-weight:600;color:var(--ink)}
.about h2{font-size:29px;font-weight:600;line-height:40px;letter-spacing:.5px}
.about h2 .accent{color:var(--brand);display:block;margin-top:2px}
.about h2 .rest{color:#444;display:block}
.about h4{margin-top:24px;color:var(--brand);font-size:14px;font-weight:600;letter-spacing:.5px;margin-left:-2px}
.about p{margin-top:8px;font-size:13.3px;line-height:23px;color:#333;text-align:justify}
.about h4.second{margin-top:24px}
.about p.long{margin-top:16px}

.photo-one{left:605px;top:1079px;width:388px;height:422px;background:linear-gradient(160deg,#d9d2c4 0%,#9a8a70 45%,#4a4036 100%)}
.photo-two{left:784px;top:1266px;width:271px;height:316px;border:7px solid var(--white);border-right:0;border-bottom:0;background:linear-gradient(150deg,#a9c4db 0%,#5f8db8 50%,#2d4f78 100%)}

.cta{left:0;top:2078px;width:1200px;height:354px;background:linear-gradient(180deg,#4d5f6e 0%,#5c6770 50%,#3f4a52 100%)}
.cta h2{position:absolute;left:0;width:1200px;top:2198px;text-align:center;color:var(--white);font-size:46px;font-weight:700;letter-spacing:1.5px}
.cta-btn{left:512px;top:2285px;width:169px;height:56px;background:var(--brand);color:var(--white);font-size:18px;font-weight:500;display:flex;align-items:center;justify-content:center;letter-spacing:.5px}

.inquiry{left:140px;top:1762px;width:919px;height:354px;background:var(--white);box-shadow:2px 0 2px rgba(0,0,0,.05)}
.inquiry h2{position:absolute;left:0;width:919px;top:52px;text-align:center;font-size:29px;font-weight:600;color:#444}
.inquiry h2 .accent{color:var(--brand)}
.inquiry .lead{position:absolute;left:0;width:919px;top:104px;text-align:center;font-size:14.5px;color:#333}
.field{position:absolute;width:254px;height:35px;border:1px solid var(--line);font-size:12px;color:#999;padding:0 14px;display:flex;align-items:center}
.submit{position:absolute;left:406px;top:264px;width:106px;height:32px;background:var(--brand);color:var(--white);font-size:13.5px;font-weight:600;display:flex;align-items:center;justify-content:center;letter-spacing:.4px}

.site-footer{left:0;top:2432px;width:1200px;height:303px;background:var(--brand)}
.footer-brand{left:0;width:1200px;top:2490px;display:flex;justify-content:center;align-items:center;gap:10px;color:var(--white);font-weight:600}
.footer-brand .brand-dot{background:var(--white)}
.footer-brand span{font-size:22px;line-height:25px;display:block}
.social{left:0;width:1200px;top:2600px;display:flex;justify-content:center;gap:22px}
.social span{width:16px;height:16px;border-radius:50%;background:var(--white);display:block}
.footer-nav{left:173px;width:853px;top:2651px;display:flex;justify-content:space-between}
.copyright{left:0;width:1200px;top:2694px;text-align:center;color:var(--white);font-size:12px}
</style>
</head>
<body>

<nav class="top-nav abs">
  <a href="#">HOME</a><a href="#">ABOUT US</a><a href="#">SCHEDULE AND COST</a><a href="#">REGISTRATION</a><a href="#">ONLINE COURSES</a><a href="#">OUR ADVANTAGE</a><a href="#">CONTACT US</a>
</nav>

<header class="site-header abs"></header>
<div class="brand-name abs"><div class="brand-dot"></div><div><span>Bright Harbor</span><span>Real Estate Institute</span></div></div>

<div class="contact-item abs" style="left:672px">
  <svg width="30" height="40" viewBox="0 0 30 40" fill="none" stroke="#3276b5" stroke-width="2"><path d="M10 4 L4 8 C2 20 8 32 18 37 L24 33 L19 26 L15 28 C11 23 10 18 11 13 L15 12 Z"/></svg>
  <div><div class="label">Call Us:</div><div class="value">1-555-204-7731</div></div>
</div>
<div class="contact-item abs" style="left:868px">
  <svg width="32" height="36" viewBox="0 0 32 36" fill="none" stroke="#3276b5" stroke-width="2"><path d="M2 12 L28 4 L30 26 L6 32 Z"/><path d="M2 12 L18 20 L28 4"/></svg>
  <div><div class="label">Mail Us:</div><div class="value">info@brightharbor.org</div></div>
</div>

<div class="hero abs" role="img" aria-label="Instructor teaching a classroom of adult students"></div>
<div class="hero-text abs">We Provide Classes For People To<br>Fulfill License Requirements &amp;<br>Continuing Education Classes<br>For Licensed Real Estate Agents</div>

<section class="feature abs" style="left:137px">
  <svg width="72" height="72" viewBox="0 0 72 72" fill="none" stroke="#3276b5" stroke-width="2.5"><rect x="18" y="6" width="48" height="34"/><circle cx="46" cy="22" r="8"/><circle cx="14" cy="30" r="6"/><path d="M6 66 V44 H22 V66"/><circle cx="36" cy="50" r="5"/><circle cx="56" cy="50" r="5"/><path d="M28 66 V60 H44 V66 M48 66 V60 H64 V66"/></svg>
  <h3>Search Live Classes</h3>
  <p>Lorem ipsum dolor sit amet, consectetuer adipiscing elit, sed diam nonummy nibh euismod tincidunt ut laoreet dolore magna aliquam erat volutpat. Ut wisi enim</p>
  <a class="learn" href="#">Learn More <svg width="14" height="10" viewBox="0 0 14 10" fill="none" stroke="#3276b5" stroke-width="1.8"><path d="M1 5 H12 M8 1 L12 5 L8 9"/></svg></a>
</section>

<section class="feature abs" style="left:460px">
  <svg width="72" height="72" viewBox="0 0 72 72" fill="none" stroke="#3276b5" stroke-width="2.5"><rect x="8" y="4" width="56" height="44" rx="3"/><path d="M16 4 V48 M56 4 V48"/><path d="M24 14 L32 19 L24 24 Z"/><path d="M36 16 H50 M36 24 H50 M24 32 H50 M24 40 H44"/><circle cx="14" cy="58" r="4"/><circle cx="29" cy="58" r="4"/><circle cx="44" cy="58" r="4"/><circle cx="59" cy="58" r="4"/><path d="M7 68 Q14 62 21 68 M22 68 Q29 62 36 68 M37 68 Q44 62 51 68 M52 68 Q59 62 66 68"/></svg>
  <h3>Online Classes</h3>
  <p>Lorem ipsum dolor sit amet, consectetuer adipiscing elit, sed diam nonummy nibh euismod tincidunt ut laoreet dolore magna aliquam erat volutpat. Ut wisi enim</p>
  <a class="learn" href="#">Learn More <svg width="14" height="10" viewBox="0 0 14 10" fill="none" stroke="#3276b5" stroke-width="1.8"><path d="M1 5 H12 M8 1 L12 5 L8 9"/></svg></a>
</section>

<section class="feature abs" style="left:780px">
  <svg width="72" height="72" viewBox="0 0 72 72" fill="none" stroke="#3276b5" stroke-width="2.5"><rect x="4" y="4" width="58" height="40" rx="2"/><rect x="12" y="12" width="18" height="14"/><path d="M36 14 H54 M36 22 H54 M12 34 H40"/><path d="M26 44 V52 H44 M4 58 H44 V66 H4 Z"/><rect x="48" y="46" width="16" height="22" rx="8"/><path d="M56 46 V54"/></svg>
  <h3>Registration</h3>
  <p>Lorem ipsum dolor sit amet, consectetuer adipiscing elit, sed diam nonummy nibh euismod tincidunt ut laoreet dolore magna aliquam erat volutpat. Ut wisi enim</p>
  <a class="learn" href="#">Learn More <svg width="14" height="10" viewBox="0 0 14 10" fill="none" stroke="#3276b5" stroke-width="1.8"><path d="M1 5 H12 M8 1 L12 5 L8 9"/></svg></a>
</section>

<section class="about abs">
  <div class="eyebrow">ABOUT</div>
  <h2><span class="accent">BRIGHT HARBOR</span><span class="rest">REAL ESTATE INSTITUTE</span></h2>
  <h4>OUR STORY</h4>
  <p>Lorem Ipsum is simply dummy text of the printing and typesetting industry. Lorem Ipsum has been the industry's standard dummy text ever since the 1500s, when an unknown printer took a galley of type and scrambled it to make a type specimen book.</p>
  <h4 class="second">OUR PROMISE</h4>
  <p class="long">It is a long established fact that a reader will be distracted by the readable content of a page when looking at its layout. The point of using Lorem Ipsum is that it has a more-or-less normal distribution of letters, as opposed to using 'Content here, content here', making it look like readable English. Many desktop publishing packages and web page editors now use Lorem Ipsum as their default model text, and a search for 'lorem ipsum' will uncover many web sites still in their infancy.</p>
</section>

<div class="photo-one abs" role="img" aria-label="Instructor lecturing a small class at a laptop"></div>
<div class="photo-two abs" role="img" aria-label="Student smiling while studying on a laptop"></div>

<div class="cta abs" role="img" aria-label="City skyline and harbor seen from above"></div>
<div class="cta"><h2>READY TO GET STARTED?</h2></div>
<div class="cta-btn abs">GET IN TOUCH</div>

<section class="inquiry abs">
  <h2><span class="accent">QUICK</span> INQUIRY</h2>
  <div class="lead">Lorem Ipsum is simply dummy text of the printing and typesetting industry.</div>
  <div class="field" style="left:64px;top:144px">First Name</div>
  <div class="field" style="left:332px;top:144px">Last Name</div>
  <div class="field" style="left:600px;top:144px">Email</div>
  <div class="field" style="left:64px;top:194px">Phone</div>
  <div class="field" style="left:332px;top:194px">Business Name</div>
  <div class="field" style="left:600px;top:194px">Business Type</div>
  <div class="submit">SUBMIT</div>
</section>

<footer class="site-footer abs"></footer>
<div class="footer-brand abs"><div class="brand-dot"></div><div><span>Bright Harbor</span><span>Real Estate Institute</span></div></div>
<div class="social abs" aria-label="Social links"><span></span><span></span><span></span><span></span></div>
<nav class="footer-nav abs">
  <a href="#">HOME</a><a href="#">ABOUT US</a><a href="#">SCHEDULE AND COST</a><a href="#">REGISTRATION</a><a href="#">ONLINE COURSES</a><a href="#">OUR ADVANTAGE</a><a href="#">CONTACT US</a>
</nav>
<div class="copyright abs">Copyright © 2019 Bright Harbor Real Estate Institute. All Rights Reserved.</div>

</body>
</html>
```